HR consultancy website - Wordpress Design Project

We need a wordpress design for a new company based in Belgium called Brivolane. We propose HR consultancy services focused on employees' engagement (motivation). We target corporations from 100 to 1000+ employees mainly in Europe.
We need a new design for our existing website (www.brivolane.eu).
We find the current design too static and outdated and we are looking for a more appealing look & feel.
Nevertheless, it has also to be sober.
The colours of the logo (dark blue, purple and light grey) should be preferrably used.
The content structure and the texts remain the same.

Target Market(s)

HR managers, general managers of SME's, higher education

Industry/Entity Type

It Company

Requirements
Must have
• No specific functionalities, except a contact form.

```html
<!DOCTYPE html>
<html lang="en">
<head>
<meta charset="utf-8">
<title>Brivolane – HR Consultancy</title>
<link href="https://fonts.googleapis.com/css2?family=Arvo:wght@400;700&family=Gelasio:wght@400;500&display=swap" rel="stylesheet">
<style>
  :root {
    --pink: #d0246b;
    --pink-soft: #fbe0ec;
    --blue: #0b4a9a;
    --blue-dark: #0d3f8a;
    --page: #f3f3f3;
    --white: #ffffff;
    --grey-line: #cfcfcf;
    --logo-grey: #c3bbb5;
    --text: #2c2c2c;
    --footer-text: #777777;
  }
  * { box-sizing: border-box; margin: 0; padding: 0; }
  html, body { width: 1200px; height: 990px; overflow: hidden; }
  body {
    position: relative;
    background: var(--page);
    font-family: "Gelasio", Georgia, serif;
    color: var(--text);
  }
  .site-header {
    position: absolute; left: 0; top: 0; width: 1200px; height: 69px;
    background: var(--white);
  }
  .brand {
    position: absolute; left: 177px; top: 14px;
    font-family: "Arvo", serif; font-weight: 400; font-size: 33px;
    letter-spacing: 1px; color: var(--logo-grey); line-height: 40px;
  }
  .main-nav { position: absolute; top: 0; left: 649px; display: flex; }
  .main-nav a {
    font-family: "Arvo", serif; font-size: 14.5px; color: var(--pink);
    text-decoration: none; line-height: 69px; margin-right: 38px;
  }
  .main-nav a.is-active {
    background: var(--pink); color: var(--white);
    width: 83px; height: 77px; text-align: center;
    border-radius: 0 0 12px 12px; margin-right: 17px;
  }
  .hero {
    position: absolute; left: 177px; top: 93px; width: 845px; height: 313px;
    border: 3px solid var(--blue-dark); border-radius: 14px; overflow: hidden;
    background: linear-gradient(180deg, #e6edf3 0%, #c9d2da 45%, #5b6878 100%);
  }
  .hero-control {
    position: absolute; left: 381px; top: 256px; width: 79px; height: 54px;
    background: var(--blue); border-radius: 10px 10px 0 0;
  }
  .headline {
    position: absolute; left: 0; top: 420px; width: 1200px; text-align: center;
    font-family: "Arvo", serif; font-weight: 400; font-size: 20px; line-height: 24px;
    color: var(--pink); letter-spacing: 0.2px;
  }
  .features { position: absolute; left: 177px; top: 464px; display: flex; gap: 7px; }
  .feature {
    width: 206px; height: 187px; border: 3px solid var(--grey-line); border-radius: 14px;
    background: linear-gradient(180deg, #ffffff 0%, var(--pink-soft) 100%);
    padding: 22px 14px 0 17px;
  }
  .feature h3, .section-title {
    font-family: "Arvo", serif; font-weight: 700; font-size: 14px; line-height: 18px;
    color: var(--blue); letter-spacing: 0; white-space: nowrap;
  }
  .feature p { margin-top: 16px; font-size: 12.5px; line-height: 18.6px; color: var(--pink); }
  .welcome { position: absolute; left: 180px; top: 664px; width: 602px; }
  .welcome p { margin-top: 17px; font-size: 10.2px; line-height: 18.6px; }
  .welcome p + p { margin-top: 18.6px; }
  .btn {
    display: block; background: var(--pink); color: var(--white);
    font-family: "Gelasio", serif; font-size: 11px; border-radius: 17px;
    height: 34px; line-height: 34px; text-align: center; border: none;
    text-decoration: none; padding: 0;
  }
  .read-more { position: absolute; left: 180px; top: 891px; width: 89px; }
  .quick-contact {
    position: absolute; left: 816px; top: 670px; width: 206px; height: 263px;
    border: 3px solid var(--grey-line); border-radius: 14px;
    background: linear-gradient(180deg, #ffffff 0%, var(--pink-soft) 100%);
    padding: 22px 0 0 16px;
  }
  .quick-contact .field {
    display: block; width: 170px; height: 26px; margin-top: 5px;
    border: 1px solid #d6d6d6; border-radius: 8px; background: var(--white);
    font-family: "Gelasio", serif; font-size: 10.5px; color: var(--text); padding: 0 15px;
  }
  .quick-contact .field-first { margin-top: 13px; }
  .quick-contact .field-message { height: 69px; padding-top: 6px; resize: none; }
  .quick-contact .field::placeholder { color: var(--text); opacity: 1; }
  .quick-contact .submit { margin-top: 3px; width: 72px; }
  .site-footer {
    position: absolute; left: 0; top: 953px; width: 1200px; height: 37px;
    background: var(--white); font-size: 10.6px; color: var(--footer-text);
  }
  .footer-links { position: absolute; left: 187px; top: 11px; }
  .footer-meta { position: absolute; right: 178px; top: 9px; display: flex; align-items: center; gap: 6px; }
  .social-dot { width: 17px; height: 17px; border-radius: 50%; display: inline-block; }
</style>
</head>
<body>
  <header class="site-header">
    <div class="brand">BRIVOLANE</div>
    <nav class="main-nav">
      <a class="is-active" href="#">Home</a>
      <a href="#">Our Mission</a>
      <a href="#">About</a>
      <a href="#">Contact</a>
    </nav>
  </header>

  <section class="hero" role="img" aria-label="Photo of a smiling business team standing in an office">
    <div class="hero-control">
      <svg width="79" height="54" viewBox="0 0 79 54" aria-hidden="true">
        <polyline points="30,15 18,28 30,41" fill="none" stroke="#fff" stroke-width="6" stroke-linejoin="round"/>
        <polyline points="49,15 61,28 49,41" fill="none" stroke="#fff" stroke-width="6" stroke-linejoin="round"/>
        <line x1="39.5" y1="8" x2="39.5" y2="54" stroke="#3a6fb5" stroke-width="1.5"/>
      </svg>
    </div>
  </section>

  <h1 class="headline">BRIVOLANE BOOSTS COMPANY PERFORMANCE</h1>

  <section class="features">
    <article class="feature"><h3>EVALUATION</h3><p>Only between 13 and 21% of employees are actively engaged in their job.</p></article>
    <article class="feature"><h3>STRATEGY</h3><p>Brivolane helps corporate leaders get the best contribution from employees.</p></article>
    <article class="feature"><h3>PROCESS</h3><p>Our ERM tool creates an HR engagement cycle to encourage line managers to take initiatives and to enhance the engagement of their team members.</p></article>
    <article class="feature"><h3>IMPACT</h3><p>Our ERM tool measures impact by creating an index which can then be used for comparison over time.</p></article>
  </section>

  <section class="welcome">
    <h2 class="section-title">WELCOME TO OUR BRIVOLANE</h2>
    <p>Lorem ipsum dolor sit amet, consectetur adipiscing elit. Phasellus dui neque, sagittis et hendrerit ullamcorper, volutpat in eros. Quisque et pretium nulla. Cras quis malesuada massa. Morbi sed augue mauris. Donec et felis vel nisl dapibus porttitor et ac lorem. Sed dolor metus, rutrum fermentum bibendum sit amet, accumsan sit amet felis. In eu tellus dui. Suspendisse lectus ante, scelerisque ut adipiscing sed, porttitor eu tellus.</p>
    <p>Aenean et felis enim, ut tristique lacus. Nam dictum semper congue. Nunc at sapien orci, sed congue tortor. Donec a tellus enim. Donec congue lectus eu quam rhoncus venenatis. Morbi in sapien leo. Pellentesque eget nunc massa. Quisque varius risus vel urna tempus non ultrices libero egestas. Lorem ipsum dolor sit amet, consectetur adipiscing elit. Integer mi purus, vehicula vitae consequat ut, lacinia id quam. Quisque viverra gravida dictum. Duis at enim ac sem rutrum aliquet. Etiam condimentum lacus non tortor laoreet tincidunt.</p>
  </section>
  <a class="btn read-more" href="#">READ MORE</a>

  <form class="quick-contact">
    <h2 class="section-title">QUICK CONTACT FORM</h2>
    <input class="field field-first" type="text" placeholder="Name">
    <input class="field" type="email" placeholder="Email Address">
    <input class="field" type="tel" placeholder="Phone Number">
    <textarea class="field field-message" placeholder="Message"></textarea>
    <button class="btn submit" type="button">SUBMIT</button>
  </form>

  <footer class="site-footer">
    <div class="footer-links">Home &nbsp;|&nbsp; Our Mission &nbsp;|&nbsp; About Us &nbsp;|&nbsp; Contact &nbsp;|</div>
    <div class="footer-meta">
      <span>© 2012 &nbsp;|&nbsp; Brivolane &nbsp;|&nbsp; All Right Reserved &nbsp;|&nbsp; Follow us</span>
      <span class="social-dot" style="background:#3b5a9a"></span>
      <span class="social-dot" style="background:#3fa9d8"></span>
      <span class="social-dot" style="background:#ee8a2c"></span>
    </div>
  </footer>
</body>
</html>
```